Bright and beautiful business card for a coach

I'm a personal and business coach based in Perth, Australia. I need a business card that whilst subtle and elegant, will stand out and appeal on a table full of cards.

My business name is Tide Mentoring and the business card must represent the warmth and brightness implied in the name, without being gimmicky. It must have a warmth and appeal and be easy to read.

I prefer clean, minimalist designs.

It must align with the feel of my website and socials: https://www.tidementoring.com.au/
https://www.instagram.com/tidementoringau/
https://www.facebook.com/tidementoringau
Updates

Hi Designers Thank you so much for taking the time to submit designs. I wonder if I could have explained myself a little better. Most of the designs that have been submitted look rather formal and many have quite corporate looking embellishments on them (to my eye). I would like softer, warmer, more organic. I’m open to people playing about and being more abstract, using softer embellishments (e.g the line drawing flowers and grasses I’ve used in my socials) incorporating other colours from my palette or like the social icons in my email signature (in PDF), perhaps playing with size/oversize, playing with the bleed. Please don’t be constrained by what I’ve already done, it merely needs to compliment. I’m sorry if I’m not using the right words or have led you astray. I’m no designer, but I’ve done my website, socials, email signature etc all myself (my logo was a design contest) and I was really hoping for my business card to be something more creative than I could have made with a template. Reminder: No black cards/sides please. Thank you 😊

Target Market(s)

Individuals, most likely but not all female. Creative thinkers. Likely professionals.

Industry/Entity Type

Business & Personal Coach

Contact Information for Business Card

(Tide Mentoring Logo) Name: Maren Delsby; Title: Business & Personal Coach; Phone number: +61 (0)438 915307; Email: maren@tidementoring.com.au; Website: https://tidementoring.com.au; Social icons for Facebook, Instagram & LinkedIn: @tidementoringAU. Optional strapline: "A thinking partner to help you cut through the noise"

Font styles to use
Sans Serif

Colors
00AB8E
00BBA5
67D7C9
C6EFE9
E9F9F6
59FF00
82FF00
B8FF75
E3FFCB
F4FFEA
FFC000
F8CF3A
FAE287
FDF2CF
FEFAEE

Requirements
Must have
• Must align with feel of my website and socials. Must have a pop of #FFC000 (possibly whole of one side, or at least a block). Bright or white background. Easy to read.
Nice to have
• Possibly incorporate the sunshine/grass picture I have used in website and socials - will upload.
Should not have
• Must not be black or dark. Not impersonal or corporate looking.

```html
<!DOCTYPE html>
<html lang="en">
<head>
<meta charset="utf-8">
<title>Tide Mentoring – Business Card</title>
<link rel="stylesheet" href="https://fonts.googleapis.com/css2?family=Arimo:wght@400;700&family=Montserrat:wght@500&display=swap">
<style>
  :root {
    --page-bg: #ecebe7;
    --card-white: #ffffff;
    --gold: #e39a1a;
    --gold-light: #f6be2a;
    --amber: #ffc000;
    --text-grey: #5e5e5e;
    --rule-grey: #9a9a9a;
    --grass-deep: #2f5a1c;
    --grass-mid: #6f9d2e;
    --grass-light: #b8d36a;
    --sun-glow: #fff3c8;
  }
  * { box-sizing: border-box; margin: 0; padding: 0; }
  html, body { width: 1200px; height: 900px; overflow: hidden; }
  body {
    background: var(--page-bg);
    font-family: "Arimo", Arial, sans-serif;
    position: relative;
  }
  .card {
    position: absolute;
    left: 280px;
    width: 640px;
    height: 390px;
    border-radius: 18px;
    overflow: hidden;
    box-shadow: 0 6px 18px rgba(0,0,0,0.12);
  }
  /* Back side */
  .card--back { top: 40px; }
  .back-photo {
    position: absolute; inset: 0;
    background:
      radial-gradient(circle at 78% 22%, var(--sun-glow) 0%, rgba(255,236,170,0.85) 10%, rgba(214,200,120,0.35) 28%, rgba(0,0,0,0) 45%),
      linear-gradient(180deg, #5f7e3a 0%, var(--grass-mid) 35%, var(--grass-light) 55%, var(--grass-mid) 72%, var(--grass-deep) 100%);
  }
  .back-logo {
    position: absolute; left: 40px; top: 40px;
    color: #ffffff;
    font-family: "Montserrat", Arial, sans-serif;
    font-weight: 500;
    font-size: 30px;
    letter-spacing: 2px;
  }
  .strapline {
    position: absolute; left: 0; right: 0; bottom: 42px;
    text-align: center;
    color: #ffffff;
    font-size: 20px;
    text-shadow: 0 1px 3px rgba(0,0,0,0.35);
  }
  /* Front side */
  .card--front {
    top: 470px;
    background: var(--card-white);
    border-bottom: 6px solid var(--amber);
  }
  .front-logo {
    position: absolute; left: 44px; top: 70px;
    display: flex; align-items: center; gap: 12px;
    color: var(--gold);
    font-family: "Montserrat", Arial, sans-serif;
    font-weight: 500;
    font-size: 32px;
    letter-spacing: 1.5px;
  }
  .front-logo .logo-dot {
    width: 16px; height: 16px; border-radius: 50%;
    background: var(--gold-light);
  }
  .portrait {
    position: absolute; right: 50px; top: 28px;
    width: 184px; height: 184px; border-radius: 50%;
    border: 3px solid var(--gold-light);
    padding: 5px; background: var(--card-white);
  }
  .portrait-fill {
    width: 100%; height: 100%; border-radius: 50%;
    background: radial-gradient(circle at 50% 45%, #d9b49a 0%, #a57a5c 45%, #5d6b55 100%);
  }
  .divider {
    position: absolute; left: 44px; top: 230px;
    width: 320px; height: 2px; background: var(--rule-grey);
  }
  .contact-list {
    position: absolute; left: 44px; top: 244px;
    list-style: none;
    color: var(--text-grey);
    font-size: 18px; line-height: 32px;
  }
  .contact-list li { display: flex; align-items: center; gap: 10px; }
  .contact-list svg { width: 16px; height: 16px; flex: none; }
  .person {
    position: absolute; right: 50px; top: 222px;
    text-align: right;
  }
  .person-name {
    color: var(--gold);
    font-size: 28px;
    letter-spacing: 0.5px;
    padding-bottom: 5px;
    border-bottom: 2px solid var(--rule-grey);
  }
  .person-title {
    color: var(--text-grey);
    font-size: 18px;
    margin-top: 6px;
  }
  .social {
    position: absolute; right: 50px; bottom: 22px;
    display: flex; align-items: center; gap: 10px;
    color: var(--text-grey); font-size: 19px;
  }
  .social-mark {
    width: 16px; height: 16px; border-radius: 3px;
    background: var(--gold-light);
  }
</style>
</head>
<body>

<section class="card card--back">
  <div class="back-photo" role="img" aria-label="Photograph of sunlit green grass with the sun glowing through trees"></div>
  <div class="back-logo">Tide Mentoring</div>
  <p class="strapline">A thinking partner to help you cut through the noise</p>
</section>

<section class="card card--front">
  <div class="front-logo"><span>Tide Mentoring</span><span class="logo-dot"></span></div>

  <div class="portrait">
    <div class="portrait-fill" role="img" aria-label="Portrait photograph of Maren Delsby"></div>
  </div>

  <div class="divider"></div>

  <ul class="contact-list">
    <li>
      <svg viewBox="0 0 24 24" aria-hidden="true"><path fill="#e39a1a" d="M6.6 10.8a15 15 0 0 0 6.6 6.6l2.2-2.2c.3-.3.7-.4 1-.2 1.1.4 2.3.6 3.6.6.6 0 1 .4 1 1V20c0 .6-.4 1-1 1A17 17 0 0 1 3 4c0-.6.4-1 1-1h3.5c.6 0 1 .4 1 1 0 1.2.2 2.4.6 3.6.1.3 0 .7-.2 1z"/></svg>
      +61 (0)438 915307
    </li>
    <li>
      <svg viewBox="0 0 24 24" aria-hidden="true"><rect x="2" y="5" width="20" height="14" rx="2" fill="#e39a1a"/><path d="M3 6l9 7 9-7" fill="none" stroke="#fff" stroke-width="1.6"/></svg>
      maren@tidementoring.com.au
    </li>
    <li>
      <svg viewBox="0 0 24 24" aria-hidden="true"><circle cx="12" cy="12" r="10" fill="#e39a1a"/><path d="M2 12h20M12 2c3 3 3 17 0 20M12 2c-3 3-3 17 0 20" fill="none" stroke="#fff" stroke-width="1.4"/></svg>
      www.tidementoring.com.au
    </li>
  </ul>

  <div class="person">
    <div class="person-name">MAREN DELSBY</div>
    <div class="person-title">Business &amp; Personal Coach</div>
  </div>

  <div class="social">
    <span class="social-mark"></span>
    <span>@tidementoringAU</span>
  </div>
</section>

</body>
</html>
```